VRP Nail Gel Polish Color Tip Swatch Label Design for SUN RAY collection

We need a label design for the color swatch that will go with our new collection of nail gel polish called SUN RAY. We are a nail and beauty supply distributor in the US selling to retail nail salons in the US only. Please also see our other project launched today: VRP Gel Nail Polish Collection for 15 ml bottle (Contest)

Target Market(s)

Retail Nail Salons in the US

Industry/Entity Type

Nail Salon

Font styles to use
Serif
Sans Serif

Colors

Designer to choose colors to be used in the design.

Requirements
Must have
• VRP Logo - this needs to be changed to all black color for letters VRP and matte gold drop for the "drop";
• SUN RAY in big font/easy to see;
• Numbers in big font/easy to see: CA1, CA2, .... CA16 on on side; and CA17, CA18, .... CA32 on the other side (as there will be 16 nail tips on each side).
• Label dimensions must be 1.875" x 9.0".
Nice to have
• possible additional wording, "Premium gel polish", "Collection"
Should not have
• no picture of SUN RAY; no overpowering graphics to make it look too busy

```html
<!DOCTYPE html>
<html lang="en">
<head>
<meta charset="utf-8">
<title>VRP SUN RAY Gel Polish Swatch Label</title>
<link rel="stylesheet" href="https://fonts.googleapis.com/css2?family=Bodoni+Moda:wght@500&family=Questrial&family=Open+Sans:wght@700;800&display=swap">
<style>
  :root {
    --backdrop: #ecd9d1;
    --label-white: #ffffff;
    --ink: #1d1a1a;
    --gold: #b89a3a;
    --gold-band: #c29b2f;
    --fold: #d9d4cf;
    --splash-teal: #5cc3c1;
    --splash-orange: #ee7a45;
    --splash-pink: #eeb3b8;
  }
  * { margin: 0; padding: 0; box-sizing: border-box; }
  html, body { width: 1200px; height: 1200px; overflow: hidden; background: var(--backdrop); }
  .canvas { position: relative; width: 1200px; height: 1200px; }

  .label {
    position: absolute; left: 93px; top: 400px;
    width: 1013px; height: 422px;
    background: var(--label-white);
    overflow: hidden;
  }

  .brand {
    position: absolute; display: flex; align-items: center;
    font-family: "Open Sans", sans-serif; font-weight: 800; color: var(--ink);
    letter-spacing: -1px; line-height: 1;
  }
  .brand-dot { border-radius: 50%; background: var(--gold); }
  .front .brand { left: 338px; top: 56px; transform: translate(-50%, -50%); font-size: 50px; gap: 6px; }
  .front .brand-dot { width: 14px; height: 14px; }
  .side .brand { right: 13px; top: 24px; transform: translateY(-50%); font-size: 15px; gap: 2px; letter-spacing: 0; }
  .side .brand-dot { width: 5px; height: 5px; }

  .title {
    position: absolute; font-family: "Bodoni Moda", serif; font-weight: 500;
    color: var(--ink); white-space: nowrap; line-height: 1;
  }
  .subtitle {
    position: absolute; font-family: "Questrial", sans-serif; color: var(--gold);
    white-space: nowrap; line-height: 1;
  }
  .front .title { left: 338px; top: 140px; transform: translateX(-50%); font-size: 86px; letter-spacing: -1px; }
  .front .subtitle { left: 338px; top: 228px; transform: translateX(-50%); font-size: 29px; }
  .side .title { right: 13px; top: 46px; font-size: 25px; }
  .side .subtitle { right: 13px; top: 74px; font-size: 10px; }

  .splash-art {
    position: absolute; left: 572px; top: 0; width: 192px; height: 354px;
    background: linear-gradient(160deg, var(--splash-teal) 0%, var(--splash-orange) 45%, var(--splash-teal) 70%, var(--splash-pink) 100%);
    opacity: 0.85;
  }
  .side-art {
    position: absolute; left: 676px; top: 0; width: 60px; height: 354px;
    background: linear-gradient(180deg, var(--splash-pink), #f4d3d4);
    opacity: 0.8;
  }

  .fold { position: absolute; left: 676px; top: 0; width: 1px; height: 422px; background: var(--fold); }

  .band {
    position: absolute; left: 0; top: 354px; width: 100%; height: 56px;
    background: var(--gold-band);
  }
  .band-word {
    position: absolute; top: 50%; transform: translate(-50%, -50%);
    font-family: "Open Sans", sans-serif; font-weight: 700; font-size: 31px;
    color: var(--label-white); letter-spacing: 1px;
  }
  .band-word.front-word { left: 338px; }
  .band-word.side-word { left: 845px; }

  .shade-column {
    position: absolute; top: 116px; height: 223px;
    border: 1px solid var(--gold); border-radius: 7px;
    list-style: none; display: flex; flex-direction: column; justify-content: space-around;
    padding: 2px 0;
    font-family: "Questrial", sans-serif; font-size: 12px; letter-spacing: 1px; color: var(--gold);
  }
  .shade-column li { padding-left: 9px; }
  .shade-column.first { left: 821px; width: 46px; }
  .shade-column.second { left: 871px; width: 48px; }
</style>
</head>
<body>
<div class="canvas">
  <div class="label">
    <div class="splash-art" role="img" aria-label="Swirling splashes of teal, orange and pink gel polish pouring from bottles"></div>
    <div class="side-art" role="img" aria-label="Pink gel polish splash continuing onto the side panel"></div>
    <div class="fold"></div>

    <section class="front">
      <div class="brand">VRP<span class="brand-dot"></span></div>
      <h1 class="title">SUN RAY</h1>
      <p class="subtitle">Gel polish Collection</p>
    </section>

    <section class="side">
      <div class="brand">VRP<span class="brand-dot"></span></div>
      <h2 class="title">SUN RAY</h2>
      <p class="subtitle">Gel polish Collection</p>
      <ul class="shade-column first">
        <li>CA1</li><li>CA2</li><li>CA3</li><li>CA4</li><li>CA5</li><li>CA6</li><li>CA7</li><li>CA8</li>
      </ul>
      <ul class="shade-column second">
        <li>CA9</li><li>CA10</li><li>CA11</li><li>CA12</li><li>CA13</li><li>CA14</li><li>CA15</li><li>CA16</li>
      </ul>
    </section>

    <div class="band">
      <span class="band-word front-word">PREMIUM</span>
      <span class="band-word side-word">PREMIUM</span>
    </div>
  </div>
</div>
</body>
</html>
```